Redesign of our brintaval.com VPS mini site

We need to a full redesign (modern, fancy and attractive) with a new logo. The site is http://www.brintaval.com/

We are open to any idea / suggestion. Content will not be much more than what is present on the actual web site. We would like to see more filler images inside the page.

Into the attached files I've included all the current web pages
Updates

Project Deadline Extended
Reason: Need more time to make a choice.

Target Market(s)

Internet Hosting

Industry/Entity Type

Internet Service Provider

Logo Text

Quarly BrinTaval

Coding

Coded - Design and coding required

Number of Pages Required

3 page

Font styles to use
Sans Serif

```html
<!DOCTYPE html>
<html lang="en">
<head>
<meta charset="utf-8">
<title>Brintaval VPS Hosting</title>
<link href="https://fonts.googleapis.com/css2?family=Cinzel:wght@700&family=Lato:wght@400;700&family=Comfortaa:wght@400;700&display=swap" rel="stylesheet">
<style>
:root{
  --hero-dark:#07090f;
  --hero-blue:#16244a;
  --ink:#2b2b2b;
  --muted:#555;
  --panel:#3a3a3a;
  --panel-dark:#2c2c2c;
  --page-gray:#ececec;
  --white:#fff;
  --blue:#1b9ad6;
  --orange:#f29a1a;
  --footer:#333;
  --footer-bar:#2a2a2a;
  --rule:#d6d6d6;
}
*{box-sizing:border-box;margin:0;padding:0}
html,body{width:765px;height:1200px;overflow:hidden}
body{position:relative;background:var(--white);font-family:'Lato',sans-serif;color:var(--ink)}
.abs{position:absolute}

/* hero */
.hero{left:0;top:0;width:765px;height:343px;background:radial-gradient(ellipse at 70% 60%,var(--hero-blue) 0%,var(--hero-dark) 60%)}
.logo{left:117px;top:11px;font-family:'Lato',sans-serif;font-weight:400;font-size:19px;color:var(--white);letter-spacing:.2px}
.nav{left:364px;top:17px;display:flex;gap:9px;font-size:7.4px;color:var(--white)}
.hero-title{left:113px;top:112px;font-family:'Cinzel',serif;font-weight:700;font-size:16.5px;line-height:24px;color:var(--white)}
.hero-text{left:113px;top:162px;width:310px;font-size:8px;line-height:14.3px;color:#e6e6e6}
.btn{height:22px;padding:0 8px;font-size:7.2px;font-weight:700;color:var(--white);display:flex;align-items:center;justify-content:center;border-radius:2px}
.btn-blue{left:113px;top:214px;width:89px;background:var(--blue)}
.btn-orange{left:214px;top:214px;width:89px;background:var(--orange)}
.server-visual{left:459px;top:93px;width:178px;height:189px;background:linear-gradient(90deg,#8d9097 0%,#2a2d33 18%,#1a1c21 50%,#3a3d44 82%,#a0a3aa 100%);border-radius:3px}

/* light band */
.band{left:0;top:343px;width:765px;height:321px;background:var(--page-gray)}
.plan{width:167px;height:77px;top:364px;background:var(--white);border:1px solid #d2d2d2;box-shadow:0 1px 3px rgba(0,0,0,.15)}
.plan-name{position:absolute;left:7px;top:10px;font-size:9.5px;font-weight:700;color:#222}
.plan-sub{position:absolute;left:7px;top:24px;font-size:7px;color:var(--muted)}
.price{position:absolute;right:5px;top:5px;width:47px;height:30px;background:var(--panel-dark);border-radius:2px;text-align:center;color:var(--orange);font-weight:700;font-size:11px;padding-top:4px}
.price small{display:block;color:var(--white);font-size:4.8px;font-weight:400;margin-top:1px}
.plan-spec{position:absolute;left:7px;top:47px;font-size:6.5px;font-weight:700;line-height:12px;color:#333}
.plan-spec span::before{content:"";display:inline-block;width:4px;height:4px;border-radius:50%;background:#555;margin-right:3px;vertical-align:1px}
.plan-btn{position:absolute;right:5px;top:50px;width:63px;height:19px;background:var(--panel-dark);color:var(--white);font-size:6.8px;font-weight:700;display:flex;align-items:center;justify-content:center;border-radius:2px}

.why-title{left:0;top:482px;width:765px;text-align:center;font-family:'Comfortaa',sans-serif;font-size:16px;color:#333}
.why-sub{left:0;top:508px;width:765px;text-align:center;font-size:6.8px;color:#444}
.feature{top:537px;width:122px;height:97px;background:var(--panel);color:var(--white);text-align:center;font-family:'Comfortaa',sans-serif;font-size:10.6px;line-height:14px}
.feature svg{display:block;margin:11px auto 6px}

/* welcome */
.welcome-title{left:117px;top:676px;font-family:'Comfortaa',sans-serif;font-size:16px;color:#333}
.welcome-text{left:117px;top:703px;width:531px;font-size:7px;line-height:12px;color:#444}
.welcome-text p+p{margin-top:12px}
.rule{left:117px;top:800px;width:531px;height:1px;background:var(--rule)}

.hosting{left:117px;top:830px;width:213px;height:171px;background:var(--panel)}
.box-head{height:28px;background:var(--panel-dark);color:var(--white);font-family:'Comfortaa',sans-serif;font-size:12px;padding:7px 9px}
.perk{position:absolute;left:9px;display:flex;gap:8px}
.perk svg{flex:none}
.perk h4{font-family:'Comfortaa',sans-serif;font-weight:400;font-size:9px;color:var(--white)}
.perk p{font-family:'Comfortaa',sans-serif;font-size:5.8px;line-height:12px;color:#ddd;width:172px}
.locations{left:345px;top:828px;width:303px;height:173px;background:var(--white);border:1px solid #ddd}
.locations .box-head{height:30px;padding-top:8px}
.map{position:absolute;left:24px;top:42px;width:255px;height:122px;background:linear-gradient(135deg,#8a8a8a,#4a4a4a);border-radius:6px;opacity:.85}

/* footer */
.footer{left:0;top:1030px;width:765px;height:139px;background:var(--footer);color:var(--white)}
.foot-head{position:absolute;top:20px;font-family:'Comfortaa',sans-serif;font-size:10px}
.contact{position:absolute;left:117px;top:45px;font-size:6.8px;font-weight:700;line-height:16px}
.news-text{position:absolute;left:298px;top:44px;width:140px;font-size:6.2px;line-height:11px}
.news-input{position:absolute;left:298px;top:73px;width:130px;height:18px;background:var(--white);color:#999;font-size:6.5px;padding:4px 5px}
.news-btn{position:absolute;left:298px;top:99px;width:71px;height:18px;background:#1e1e1e;font-size:7px;font-weight:700;display:flex;align-items:center;justify-content:center}
.social{position:absolute;left:481px;top:47px;display:flex;gap:12px}
.social span{width:14px;height:14px;background:var(--white);border-radius:2px}
.bottom-bar{left:0;top:1169px;width:765px;height:31px;background:var(--footer-bar);color:#ccc;font-size:6.8px}
.bottom-nav{position:absolute;left:117px;top:12px;display:flex;gap:9px}
.copyright{position:absolute;right:117px;top:12px}
</style>
</head>
<body>

<header class="abs hero">
  <div class="abs logo">brintaval</div>
  <nav class="abs nav"><span>Linux VPS</span><span>Windows VPS</span><span>Dedicated</span><span>Servers</span><span>About Us</span><span>Specials</span><span>Contact Us</span></nav>
  <h1 class="abs hero-title">CHECK OUR NEWER LOWER PRICES<br>SAME GREAT QUALITY...</h1>
  <p class="abs hero-text">We offer high performance, 99.9% guaranteed uptime, 24/7 North American based support and awesome pricing.HarborlineVPS.net is your one-stop hosting partner. Contact our sales department for more information.</p>
  <div class="abs btn btn-blue">Virtual Private Servers</div>
  <div class="abs btn btn-orange">Dedicated Server</div>
  <div class="abs server-visual" role="img" aria-label="Open server rack cabinet with glowing drive bays"></div>
</header>

<section class="abs band"></section>

<article class="abs plan" style="left:117px">
  <div class="plan-name">OPENVZ VPS</div><div class="plan-sub">Linux VPS for the masses</div>
  <div class="price">$5.00<small>PER MONTH</small></div>
  <div class="plan-spec"><span>128MB RAM</span><br><span>1 IP Address</span></div>
  <div class="plan-btn">VIEW PLANS</div>
</article>
<article class="abs plan" style="left:299px">
  <div class="plan-name">KVM VPS</div><div class="plan-sub">True Isolation - Premium VPS</div>
  <div class="price">$5.00<small>PER MONTH</small></div>
  <div class="plan-spec"><span>512MB RAM</span><br><span>1 IP Address</span></div>
  <div class="plan-btn">VIEW PLANS</div>
</article>
<article class="abs plan" style="left:481px">
  <div class="plan-name">DEDICATED</div><div class="plan-sub">E-Commerce &amp; High Traffic</div>
  <div class="price">$55.00<small>PER MONTH</small></div>
  <div class="plan-spec"><span>4GB RAM</span><br><span>1 IP Address</span></div>
  <div class="plan-btn">VIEW PLANS</div>
</article>

<h2 class="abs why-title">Why Choose Brintaval</h2>
<p class="abs why-sub">HarborlineVPS strives to provide affordable VPS services without compromising on quality</p>

<div class="abs feature" style="left:117px">
  <svg width="30" height="36" viewBox="0 0 30 36"><path d="M8 15V10a7 7 0 0 1 14 0v5" fill="none" stroke="#fff" stroke-width="3"/><rect x="3" y="15" width="24" height="19" rx="2" fill="#fff"/><circle cx="15" cy="23" r="3" fill="#3a3a3a"/><rect x="14" y="24" width="2" height="6" fill="#3a3a3a"/></svg>
  Security is Our<br>Top Priority
</div>
<div class="abs feature" style="left:253px">
  <svg width="36" height="36" viewBox="0 0 36 36"><path d="M5 20a13 13 0 0 1 26 0" fill="none" stroke="#fff" stroke-width="3"/><rect x="2" y="18" width="7" height="11" rx="2" fill="#fff"/><rect x="27" y="18" width="7" height="11" rx="2" fill="#fff"/><circle cx="18" cy="22" r="9" fill="none" stroke="#fff" stroke-width="2.5"/></svg>
  24x7<br>Customer
</div>
<div class="abs feature" style="left:390px">
  <svg width="36" height="36" viewBox="0 0 36 36"><circle cx="24" cy="11" r="8" fill="none" stroke="#fff" stroke-width="3.5"/><path d="M18 17L5 30l3 3 3-3 2 2 3-3-2-2 6-6" fill="#fff"/></svg>
  Full Root<br>Access
</div>
<div class="abs feature" style="left:526px">
  <svg width="36" height="36" viewBox="0 0 36 36"><circle cx="18" cy="20" r="13" fill="#fff"/><path d="M18 2a7 7 0 0 0-7 7c0 5 7 12 7 12s7-7 7-12a7 7 0 0 0-7-7z" fill="#3a3a3a" stroke="#fff" stroke-width="1.5"/><circle cx="18" cy="9" r="2.5" fill="#fff"/></svg>
  Solid &amp; Superior<br>Network
</div>

<h2 class="abs welcome-title">Welcome to Brintaval</h2>
<div class="abs welcome-text">
  <p>Brintaval net was started with one primary goal in mind; offer reasonably priced high quality VPS hosting solutions from 6 different world-class datacenter locations across the US. Our entire infrastructure is built for performance, with only the highest grade enterprise class servers and network equipment utilized. Managed by a group of tech junkies with an acute sense for business, HarborlineVPS.net is built to please even the most particular customers.</p>
  <p>With multiple offerings such as Windows VPS, KVM VPS, Linux VPS, and DDoS Protected VPS, we are a one stop shop for all your needs. Our corporate culture is that of accountability, a fact which is obvious throughout all aspects of our company. The sooner you switch to HarborlineVPS.net, the more quickly you'll realize what you've been missing.</p>
</div>
<div class="abs rule"></div>

<section class="abs hosting">
  <div class="box-head">Hosting Plans Just For You</div>
  <div class="perk" style="top:35px">
  <svg width="26" height="28" viewBox="0 0 26 28"><rect x="2" y="2" width="22" height="6" fill="#fff"/><rect x="2" y="10" width="22" height="6" fill="#fff"/><rect x="2" y="18" width="22" height="6" fill="#fff"/></svg>
    <div><h4>Stable &amp; Reliable Servers</h4><p>HarborlineVPS utilizes high performance Corvane Xr<br>processors with RAID10 arrays</p></div>
  </div>
  <div class="perk" style="top:80px">
  <svg width="26" height="28" viewBox="0 0 26 28"><rect x="2" y="18" width="4" height="8" fill="#fff"/><rect x="8" y="14" width="4" height="12" fill="#fff"/><rect x="14" y="10" width="4" height="16" fill="#fff"/><rect x="20" y="6" width="4" height="20" fill="#fff"/><path d="M2 14L10 7l5 3 9-8" fill="none" stroke="#fff" stroke-width="1.5"/></svg>
    <div><h4>99% Uptime Guarantee!</h4><p>HarborlineVPS utilizes high performance Corvane Xr<br>processors with RAID10 arrays</p></div>
  </div>
  <div class="perk" style="top:126px">
  <svg width="26" height="28" viewBox="0 0 26 28"><path d="M6 22a6 6 0 0 1 0-12 8 8 0 0 1 15 2 5 5 0 0 1 0 10z" fill="#fff"/></svg>
    <div><h4>24/7 Support</h4><p>HarborlineVPS utilizes high performance Corvane Xr<br>processors with RAID10 arrays</p></div>
  </div>
</section>

<section class="abs locations">
  <div class="box-head">Brintaval Dataceanter Locations</div>
  <div class="map" role="img" aria-label="Striped world map showing datacenter regions"></div>
</section>

<footer class="abs footer">
  <div class="foot-head" style="left:117px">CONTACT INFO</div>
  <div class="contact">L7, 52 CORRAN STREET, SYDNEY, NSW 2000,<br>AUSTRALIA<br>ACN 412 803 557 | AFSL 590218<br>EMAIL: SUPPORT@BRINTAVAL.COM<br>TEL: +61 2 5550 1274</div>
  <div class="foot-head" style="left:298px">SIGNUP NESLATTER</div>
  <p class="news-text">It is a long established fact that a reader will be distracted by the readable</p>
  <div class="news-input">Enter Name</div>
  <div class="news-btn">SUBSCRIB</div>
  <div class="foot-head" style="left:481px">FOLOW LINK</div>
  <div class="social" aria-label="Social links"><span></span><span></span><span></span></div>
</footer>
<div class="abs bottom-bar">
  <nav class="bottom-nav"><span>Linux VPS</span><span>Windows VPS</span><span>Dedicated</span><span>Servers</span><span>About Us</span><span>Specials</span><span>Contact Us</span></nav>
  <div class="copyright">© 2015 Brintaval All Rights Reserved.</div>
</div>

</body>
</html>
```